We need visit card and a letter paper for our website. thx

We have a beauty clinic in Switzerland.
https://wolkenbachtal.ch
We need a visit card.

Requirements
Must have
• see colors on website

```html
<!DOCTYPE html>
<html lang="en">
<head>
<meta charset="utf-8">
<title>Wolkenbachtal Beauty Clinic – Business Card</title>
<link href="https://fonts.googleapis.com/css2?family=Arimo:wght@400;700&display=swap" rel="stylesheet">
<style>
  :root {
    --magenta: #d427b3;
    --pink: #fbc6f0;
    --pink-soft: #f9c5ee;
    --page: #f4f5f4;
    --ink: #141414;
    --white: #ffffff;
  }
  * { margin: 0; padding: 0; box-sizing: border-box; }
  html, body { width: 960px; height: 1200px; overflow: hidden; background: var(--page); }
  body { position: relative; font-family: "Arimo", Arial, sans-serif; color: var(--ink); }

  .card { position: absolute; overflow: hidden; }
  .card-front { left: 66px; top: 75px; width: 840px; height: 481px; background: var(--white); }
  .card-back { left: 65px; top: 654px; width: 840px; height: 480px; background: var(--magenta); }

  .front-art { position: absolute; left: 0; top: 0; width: 840px; height: 481px; }

  .brand { position: absolute; left: 20px; top: 40px; }
  .brand-name { font-size: 30px; font-weight: 400; color: var(--ink); letter-spacing: -0.3px; }
  .brand-sub { font-size: 9px; letter-spacing: 3px; color: var(--ink); margin-top: 4px; padding-left: 52px; }

  .person { position: absolute; left: 39px; top: 152px; }
  .person-name { font-size: 24px; }
  .person-role { font-size: 16px; margin-top: 10px; }

  .contacts { position: absolute; left: 382px; top: 78px; list-style: none; }
  .contact { position: relative; display: flex; align-items: flex-start; height: 37px; font-size: 20px; line-height: 24px; }
  .contact-icon { width: 28px; height: 28px; border-radius: 50%; background: var(--pink); margin-right: 10px; margin-top: -3px; display: flex; align-items: center; justify-content: center; flex: none; }
  .contact-icon svg { width: 16px; height: 16px; }
  .hotline-note { font-size: 14.5px; color: var(--magenta); margin-left: 12px; margin-top: 3px; }

  .web-band { position: absolute; left: 0; top: 426px; width: 840px; height: 55px; background: var(--magenta); color: var(--white); font-size: 19px; }
  .web-item { position: absolute; top: 13px; display: flex; align-items: center; }
  .web-item .contact-icon { background: var(--pink); margin-top: 0; }
  .web-site { left: 53px; }
  .web-mail { left: 498px; }
  .web-divider { position: absolute; left: 418px; top: 13px; font-size: 20px; }

  .services-title { position: absolute; left: 0; width: 840px; top: 49px; text-align: center; font-size: 24px; font-weight: 700; color: var(--pink-soft); }
  .services { position: absolute; top: 138px; list-style: none; color: var(--white); font-size: 23px; }
  .services-left { left: 120px; }
  .services-right { left: 497px; }
  .services li { height: 51px; display: flex; align-items: center; }
  .services li::before { content: "*"; color: var(--pink-soft); font-size: 22px; width: 28px; padding-top: 6px; }

  .tagline { position: absolute; left: 0; top: 426px; width: 840px; height: 54px; background: var(--pink); color: var(--magenta); font-size: 19px; text-align: center; line-height: 54px; }
</style>
</head>
<body>

<section class="card card-front">
  <svg class="front-art" viewBox="0 0 840 481" xmlns="http://www.w3.org/2000/svg">
    <defs>
      <linearGradient id="photo-tone" x1="0" y1="0" x2="1" y2="1">
        <stop offset="0" stop-color="#fbc6f0"/>
        <stop offset="0.55" stop-color="#f6c9dc"/>
        <stop offset="1" stop-color="#fbc6f0"/>
      </linearGradient>
    </defs>
    <rect x="0" y="0" width="840" height="11" fill="#fbc6f0"/>
    <path role="img" aria-label="Photo of a woman in swimwear reclining across the card" d="M0 248 C60 232 110 228 150 232 C260 242 380 290 520 292 C660 294 790 240 840 150 L840 430 L0 430 Z" fill="url(#photo-tone)"/>
    <path d="M0 248 C60 232 110 228 150 232 C260 242 380 290 520 292 C660 294 790 240 840 150 L840 137 C790 225 660 278 520 278 C380 278 260 228 150 222 C100 219 50 225 0 241 Z" fill="#d427b3"/>
  </svg>

  <div class="brand">
    <div class="brand-name">Wolkenbachtal</div>
    <div class="brand-sub">BEAUTY CLINIC</div>
  </div>

  <div class="person">
    <div class="person-name">Dr. Lena Marbach</div>
    <div class="person-role">Designation - If any</div>
  </div>

  <ul class="contacts">
    <li class="contact">
      <span class="contact-icon"><svg viewBox="0 0 16 16"><rect x="4.5" y="1.5" width="7" height="13" rx="1.5" fill="none" stroke="#d427b3" stroke-width="1.4"/><line x1="7" y1="12.3" x2="9" y2="12.3" stroke="#d427b3" stroke-width="1.2"/></svg></span>
      + 00 123 456 XXX
    </li>
    <li class="contact">
      <span class="contact-icon"><svg viewBox="0 0 16 16"><path d="M4 1.5 L6.5 4.5 L5 6.5 C6 8.8 7.2 10 9.5 11 L11.5 9.5 L14.5 12 L12.5 14.5 C7 14 2 9 1.5 3.5 Z" fill="#d427b3"/></svg></span>
      + 41 (0) 800 22 30 40<span class="hotline-note">Free 24-hour beauty hotline</span>
    </li>
    <li class="contact" style="height:auto">
      <span class="contact-icon"><svg viewBox="0 0 16 16"><rect x="2" y="4" width="12" height="8.5" fill="none" stroke="#d427b3" stroke-width="1.3"/><path d="M2 4 L8 9 L14 4" fill="none" stroke="#d427b3" stroke-width="1.3"/></svg></span>
      <span>Talweg 14, 7550 Bergmatt,<br>Switzerland</span>
    </li>
  </ul>

  <div class="web-band">
    <div class="web-item web-site">
      <span class="contact-icon"><svg viewBox="0 0 16 16" fill="none" stroke="#d427b3" stroke-width="1.1"><circle cx="8" cy="8" r="6"/><ellipse cx="8" cy="8" rx="2.6" ry="6"/><line x1="2" y1="8" x2="14" y2="8"/><line x1="3" y1="5" x2="13" y2="5"/><line x1="3" y1="11" x2="13" y2="11"/></svg></span>
      www.wolkenbachtal.ch
    </div>
    <span class="web-divider">|</span>
    <div class="web-item web-mail">
      <span class="contact-icon"><svg viewBox="0 0 16 16"><text x="8" y="12.5" text-anchor="middle" font-family="Arimo, Arial, sans-serif" font-size="13" fill="#d427b3">@</text></svg></span>
      hallo@wolkenbachtal.ch
    </div>
  </div>
</section>

<section class="card card-back">
  <h2 class="services-title">Our services</h2>
  <ul class="services services-left">
    <li>Breast augmentation</li>
    <li>Breast implants</li>
    <li>Breast lift</li>
    <li>Breast reduction</li>
  </ul>
  <ul class="services services-right">
    <li>Nipple correction</li>
    <li>Autologous fat transfer</li>
    <li>Liposuction</li>
    <li>Labia correction</li>
  </ul>
  <p class="tagline">Beauty clinic Wolkenbachtal - your expert for plastic and aesthetic surgery</p>
</section>

</body>
</html>
```